New landing page for book

Redesign http://www.quandelfieldworks.com so it looks more cutting edge and perhaps have buttons for the online bookstores.

Also I may soon have a trailer video produced so it Would be great to see an option with space for where a video might go and an option as the site is now without a video. Thanks

Industry/Entity Type

Online

Number of Pages Required

1 page

Colors

Designer to choose colors to be used in the design.

```html
<!DOCTYPE html>
<html lang="en">
<head>
<meta charset="utf-8">
<title>Vornatha — International Financial Crime Thriller</title>
<link href="https://fonts.googleapis.com/css2?family=Roboto:wght@300;400;500;700;900&display=swap" rel="stylesheet">
<style>
:root{
  --blue:#1c55c8;
  --blue-deep:#123f9e;
  --white:#ffffff;
  --ink:#333333;
  --muted:#555555;
  --star:#f0561c;
  --footer:#333333;
}
*{box-sizing:border-box;margin:0;padding:0}
html,body{width:698px;height:1200px;overflow:hidden;background:var(--white)}
body{font-family:'Roboto',Arial,sans-serif;color:var(--ink);position:relative}
.page{position:relative;width:698px;height:1200px;overflow:hidden}

/* hero */
.hero{position:absolute;left:0;top:0;width:698px;height:330px}
.hero-bg{position:absolute;left:0;top:0}
.nav{position:absolute;top:16px;left:478px;display:flex;gap:10px;font-size:6.5px;font-weight:500;color:var(--white)}
.nav .caret{display:inline-block;margin-left:3px;border:2.5px solid transparent;border-top:3px solid var(--white);vertical-align:-1px}
.eyebrow{position:absolute;left:145px;top:60px;font-size:11px;font-weight:400;color:var(--white)}
.title{position:absolute;left:144px;top:72px;font-size:29px;font-weight:700;color:var(--white);letter-spacing:-.3px}
.stores{position:absolute;left:145px;top:121px;display:flex;gap:4px}
.store{width:31px;height:31px;border-radius:3px;display:flex;align-items:center;justify-content:center;font-size:5px;font-weight:500;color:var(--white)}
.store.s1{background:#111}
.store.s2{background:#3d8a4e}
.store.s3,.store.s4,.store.s6{background:var(--white);color:var(--ink)}
.store.s5{background:#f58a1f}
.btn{position:absolute;display:flex;align-items:center;justify-content:center;background:var(--white);color:var(--blue);font-size:7px;font-weight:700;border-radius:2px;letter-spacing:.3px}
.btn.hero-btn{left:145px;top:168px;width:110px;height:31px}
.book{position:absolute;left:362px;top:48px;width:206px;height:278px}

/* intro */
.intro{position:absolute;left:0;top:373px;width:698px;text-align:center;color:var(--blue)}
.intro h2{font-size:18px;line-height:18.5px;font-weight:400}
.intro h2 strong{font-weight:700}
.intro p{margin:11px auto 0;width:340px;font-size:5.3px;line-height:8.5px;color:var(--muted)}

/* story */
.story{position:absolute;left:145px;top:497px;width:180px;font-size:5.2px;line-height:8.6px;color:var(--muted);text-align:justify}
.story p{margin-bottom:6.5px}
.story-art{position:absolute;left:336px;top:497px}

/* reviews */
.reviews-title{position:absolute;left:0;top:760px;width:698px;text-align:center;font-size:18px;font-weight:500;color:var(--blue)}
.review{position:absolute;background:var(--white);box-shadow:0 1px 5px rgba(0,0,0,.25);border-radius:2px;text-align:center;padding:0 12px;display:flex;flex-direction:column;justify-content:center;font-size:8px;line-height:11px;font-weight:300;color:var(--ink)}
.review .who{margin-top:8px;font-weight:500;font-size:8px}
.review .stars{color:var(--star);font-size:8px;letter-spacing:1px;line-height:10px}
.review.r1{left:145px;top:822px;width:130px;height:139px}
.review.r2{left:284px;top:809px;width:130px;height:165px;background:var(--blue);color:var(--white)}
.review.r2 .stars{color:var(--white)}
.review.r3{left:423px;top:822px;width:130px;height:139px}

/* release */
.release{position:absolute;left:0;top:1023px;width:698px;height:132px;background:linear-gradient(180deg,var(--blue),var(--blue-deep) 140%);text-align:center;color:var(--white)}
.release h3{margin-top:25px;font-size:18px;font-weight:700}
.release .email{margin-top:7px;font-size:9px;letter-spacing:2.2px;font-weight:400}
.btn.release-btn{left:295px;top:72px;width:109px;height:36px}

/* footer */
.footer{position:absolute;left:0;top:1155px;width:698px;height:45px;background:var(--footer)}
.copy{position:absolute;left:145px;top:14px;font-size:5px;line-height:9px;color:#ccc}
.copy strong{color:var(--white);font-weight:700}
.social{position:absolute;left:422px;top:9px;display:flex;gap:3px}
.social span{width:24px;height:24px;border-radius:50%;border:2px solid var(--white);display:flex;align-items:center;justify-content:center;font-size:4.5px;font-weight:500;color:var(--white)}
</style>
</head>
<body>
<div class="page">

  <header class="hero">
    <svg class="hero-bg" width="698" height="330" viewBox="0 0 698 330">
      <defs>
        <linearGradient id="heroBlue" x1="0" y1="0" x2="0" y2="1">
          <stop offset="0" stop-color="#1a50c4"/>
          <stop offset="1" stop-color="#1e5ad0"/>
        </linearGradient>
      </defs>
      <path d="M0 0H698V225C660 280 620 305 570 300C500 295 440 285 370 285C310 280 260 232 190 232C110 232 50 245 0 260Z" fill="url(#heroBlue)"/>
    </svg>
    <nav class="nav"><span>Buy Now<i class="caret"></i></span><span>Contact us</span></nav>
    <p class="eyebrow">International Financial</p>
    <h1 class="title">Crime Thriller</h1>
    <div class="stores">
      <span class="store s1">Arvelo</span>
      <span class="store s2">Bindery</span>
      <span class="store s3">Kelo</span>
      <span class="store s4">Playdeck</span>
      <span class="store s5">Pageleaf</span>
      <span class="store s6">Wordmint</span>
    </div>
    <a class="btn hero-btn">BUY NOW!</a>
    <svg class="book" viewBox="0 0 206 278" role="img" aria-label="Book cover of Vornatha by Marcus Hale: an armed operative facing a domed capital skyline">
      <defs>
        <linearGradient id="coverTone" x1="0" y1="0" x2="1" y2="1">
          <stop offset="0" stop-color="#6b4a2a"/>
          <stop offset=".5" stop-color="#3b4a40"/>
          <stop offset="1" stop-color="#1f302c"/>
        </linearGradient>
      </defs>
      <rect x="6" y="6" width="192" height="272" fill="rgba(0,0,0,.15)"/>
      <rect x="0" y="0" width="148" height="276" fill="url(#coverTone)"/>
      <rect x="148" y="2" width="12" height="272" fill="#e6e6e6"/>
      <rect x="160" y="0" width="44" height="276" fill="#2b3b37"/>
    </svg>
  </header>

  <section class="intro">
    <h2><strong>ATMs have shuttered. Stock markets have gone</strong><br>haywire. Can one operative stop a deadly band of<br>criminals before it is too late?</h2>
    <p>German intelligence operative Anselm Kerrig has been asked to investigate the cyber crime gang who sparked massive unrest in Kenya by taking over electronic transactions. But as he digs deeper, a wiretap on hacker communications reveals this is only the beginning</p>
  </section>

  <section class="story">
    <p>Vornatha, a shadowy criminal cabal, has launched a massive cyber attack on the United States.</p>
    <p>Taking off for Washington, Kerrig unexpectedly teams up with American gun for hire, Dane Whitcombe, and dives head-first into a massive conspiracy that reaches all the way up to the very top of the U.S. GovernmentVornatha, a shadowy criminal cabal, has launched a massive cyber attack on the United States.</p>
    <p>Taking off for Washington, Kerrig unexpectedly teams up with American gun for hire, Dane Whitcombe, and dives head-first into a massive conspiracy that reaches all the way up to the very top of the U.S. GovernmentVornatha, a shadowy criminal cabal, has launched a massive cyber attack on the United States.</p>
    <p>Stock markets have gone haywire. ATMs have shuttered. And Anselm Kerrig is about to come face to face with the men he is sent to find....</p>
    <p>From the deadly streets of Budapest to the equally perilous corridors of Washington, Vornatha is an action-packed, compulsive thriller that depicts a financial scam terrifyingly close to reality</p>
  </section>
  <svg class="story-art" width="220" height="220" viewBox="0 0 220 220" role="img" aria-label="Cover artwork detail: an operative with a pistol before a domed city skyline at sunset">
    <defs>
      <radialGradient id="artTone" cx=".6" cy=".4" r=".7">
        <stop offset="0" stop-color="#c99350"/>
        <stop offset=".5" stop-color="#5a5040"/>
        <stop offset="1" stop-color="#2a3a36"/>
      </radialGradient>
    </defs>
    <circle cx="110" cy="110" r="106" fill="url(#artTone)" stroke="#1c55c8" stroke-width="4"/>
  </svg>

  <h2 class="reviews-title">In The Words of Reviewers</h2>
  <article class="review r1">
    <p>Hale's fast-paced novel is reinforced by its skilled characters</p>
    <p class="who">Halverd Reviews</p>
    <p class="stars">★★★★★</p>
  </article>
  <article class="review r2">
    <p>"In a world ravaged by international turmoil and uncertainty for the future, author Marcus Hale presents Vornatha, an intense and politically charged novel that is both timely</p>
    <p class="who">Reader</p>
    <p class="stars">★★★★★</p>
  </article>
  <article class="review r3">
    <p>I give Vornatha by Marcus Hale a definite four out of four stars. The action is fast paced so that it keeps you wanting to see what comes next.</p>
    <p class="who">ReadersCircleHub</p>
    <p class="stars">★★★★★</p>
  </article>

  <section class="release">
    <h3>Released September 22, 2017</h3>
    <p class="email">help@quandelfieldworks.com</p>
    <a class="btn release-btn">BUY NOW!</a>
  </section>

  <footer class="footer">
    <p class="copy">© Copyright 2017 <strong>Marcus Hale</strong> · All Rights Reserved</p>
    <div class="social">
      <span>Pelro</span><span>Tivly</span><span>Ornet</span><span>Wexa</span><span>Yubo</span>
    </div>
  </footer>

</div>
</body>
</html>
```